Velvet Heron Website

We need a website for our software / project management services company based in South Africa called "Velvet Heron". We provide professional services to high value clients in the public and private sectors.

The website must present a highly professional company that exudes quality and confidence.

The theme should be a highly professional subdued look with a fairly limited palette. The neutral tone should be slightly offset with the colours from the company logo. The website should not look dead though, and subtle colour highligting should provide a fresh vibrant feel.

Refer to the current website for general content (www.velvetheron-example.co.za) that may be used. We would also like to make use of social integration and google maps.
Updates

Thanks to all the designers that have participated so far and to those that are cooking something up at this very minute :-)

We have received a lot of designs with elements that we absolutely love. So now the hard work of refining these designs can begin.

We'll try and provide feedback on every design received so far ... and await the beautiful designs that we haven't received yet :-)

Good Luck!

Reason: After careful consideration we are extending the deadline to make small revisions to some of the designs and to select the top three designs. Thank you for everyone who has made a contribution so far - we have several designs that we like and selecting the best one is proving to be difficult :-)

Target Market(s)

The company deals mostly with other businesses, so mostly B2B.

Industry/Entity Type

Software

Requirements
Nice to have
• Social integration

```html
<!DOCTYPE html>
<html lang="en">
<head>
<meta charset="utf-8">
<title>Velvet Heron – About Us</title>
<link href="https://fonts.googleapis.com/css2?family=Arimo:ital,wght@0,400;0,700;1,700&display=swap" rel="stylesheet">
<style>
  :root {
    --white: #ffffff;
    --page-grey: #9c9da1;
    --panel-edge: #b9babd;
    --logo-grey: #6d6e71;
    --brand-green: #8cc63f;
    --banner-top: #62b6d2;
    --banner-bottom: #3f95b6;
    --text-grey: #666668;
    --heading-grey: #9a9a9c;
    --ink: #1a1a1a;
    --rule: #d6d6d8;
    --map-blue: #a9bed6;
    --map-frame: #4b8fbf;
  }
  * { box-sizing: border-box; margin: 0; padding: 0; }
  html, body { width: 1200px; height: 1024px; overflow: hidden; }
  body {
    position: relative;
    font-family: "Arimo", Arial, sans-serif;
    background: linear-gradient(to bottom, var(--white) 0, var(--white) 226px, var(--page-grey) 226px);
  }
  .brand {
    position: absolute; left: 440px; top: 86px;
    display: flex; align-items: center; gap: 16px;
  }
  .brand-dot { width: 22px; height: 22px; border-radius: 50%; background: var(--brand-green); }
  .brand-name { font-size: 62px; font-weight: 700; color: var(--logo-grey); letter-spacing: -1px; }

  .main-nav {
    position: absolute; left: 161px; top: 203px; width: 878px; height: 46px;
    border: 1px solid #c4c4c6; border-radius: 4px;
    background: linear-gradient(#ffffff, #efeff0);
    display: flex; align-items: stretch;
  }
  .main-nav a {
    font-size: 13px; color: #111; text-decoration: none;
    display: flex; align-items: center; justify-content: center;
  }
  .nav-home { width: 80px; border-right: 1px solid #666; margin: 4px 0; }
  .nav-company { width: 120px; }
  .nav-services { width: 188px; background: linear-gradient(#f1f1f2, #c9c9cb); color: #555 !important; }
  .nav-portfolio { width: 130px; }
  .nav-contact { width: 100px; }
  .social { position: absolute; right: 10px; top: 6px; display: flex; gap: 6px; }
  .social span {
    width: 32px; height: 32px; border-radius: 6px;
    background: linear-gradient(#9a9a9c, #5d5d60); border: 1px solid #8a8a8c;
  }
  .crumb { position: absolute; left: 164px; top: 259px; font-size: 12px; color: var(--white); }

  .about-panel {
    position: absolute; left: 161px; top: 279px; width: 878px; height: 468px;
    border: 1px solid var(--panel-edge); border-radius: 4px; overflow: hidden;
    background: linear-gradient(#ffffff 0, #ffffff 60%, #e4e4e6 100%);
  }
  .panel-cap { height: 21px; background: linear-gradient(#f0f0f1, #e1e1e3); }
  .hero {
    position: relative; height: 117px;
    background: linear-gradient(var(--banner-top), var(--banner-bottom));
  }
  .hero h1 {
    position: absolute; left: 41px; top: 20px;
    font-size: 34px; line-height: 39px; font-weight: 700; color: var(--white); letter-spacing: 1px;
  }
  .hero-visual {
    position: absolute; right: 28px; top: 0; width: 180px; height: 117px;
    background: radial-gradient(circle at 55% 40%, #b7e0ee, #5fb0cf 70%, transparent);
  }
  .lead {
    position: absolute; left: 41px; top: 155px;
    font-size: 20px; line-height: 25px; font-style: italic; font-weight: 700;
    color: var(--heading-grey); letter-spacing: 0.6px;
  }
  .divider { position: absolute; left: 38px; top: 219px; width: 800px; height: 1px; background: var(--rule); }
  .body-copy {
    position: absolute; left: 41px; top: 237px; width: 800px;
    font-size: 16px; line-height: 20.6px; color: var(--text-grey); letter-spacing: 1.05px;
  }
  .body-copy p + p { margin-top: 20px; }

  .features {
    position: absolute; left: 161px; top: 764px; width: 878px; height: 205px;
    border: 1px solid var(--panel-edge); display: flex;
    background: linear-gradient(#ffffff 60%, #e6e6e8);
  }
  .feature { position: relative; width: 215px; border-right: 1px solid #e0e0e2; }
  .feature-head { display: flex; align-items: center; gap: 10px; padding: 14px 0 0 9px; height: 50px; }
  .feature-head h2 { font-size: 14px; font-style: italic; font-weight: 700; color: var(--heading-grey); letter-spacing: 1px; }
  .feature p { padding: 9px 8px 0 12px; font-size: 12px; line-height: 14.5px; color: var(--ink); }
  .read-more { position: absolute; right: 12px; bottom: 4px; font-size: 12px; color: var(--ink); }
  .map-block { flex: 1; position: relative; }
  .map-block h2 {
    text-align: center; margin-top: 9px;
    font-size: 14px; font-style: italic; font-weight: 700; color: var(--brand-green); letter-spacing: 0.6px;
  }
  .map-area {
    position: absolute; left: 19px; top: 33px; width: 194px; height: 163px;
    border: 1px solid var(--map-frame);
    background: linear-gradient(100deg, #c9d7b8 0, #d9dcc8 45%, var(--map-blue) 70%);
  }

  .footer-nav {
    position: absolute; left: 0; top: 977px; width: 1200px; text-align: center;
    font-size: 12px; color: var(--ink);
  }
  .footer-nav span { margin: 0 6px; }
</style>
</head>
<body>
  <header class="brand">
    <span class="brand-dot"></span>
    <span class="brand-name">Velvet Heron</span>
  </header>

  <nav class="main-nav">
    <a class="nav-home" href="#">HOME</a>
    <a class="nav-company" href="#">COMPANY</a>
    <a class="nav-services" href="#">PROFESSIONAL SERVICES</a>
    <a class="nav-portfolio" href="#">PORTFOLIO</a>
    <a class="nav-contact" href="#">CONTACT US</a>
    <div class="social" aria-label="Social links">
      <span role="img" aria-label="Social network link"></span>
      <span role="img" aria-label="Social network link"></span>
      <span role="img" aria-label="Social network link"></span>
    </div>
  </nav>

  <div class="crumb">About Us</div>

  <main class="about-panel">
    <div class="panel-cap"></div>
    <section class="hero">
      <h1>Velvet Heron is<br>a premium ICT solutions provider</h1>
      <div class="hero-visual" role="img" aria-label="Photo of a hand touching floating digital screens"></div>
    </section>
    <p class="lead">which delivers quality software development support services to clients<br>in all sectors of industry.</p>
    <div class="divider"></div>
    <div class="body-copy">
      <p>Our value proposition builds on customers' needs to successfully implement software development projects within a given set of time, quality and budgetary constraints. Our focus is to provide customers with a full set of products and services to support each phase of the software development lifecycle whilst offering the benefits of flexibility in scaling of resources, cost reduction, improved cost management, access to specialized skills and the ability to focus on strategic business needs.</p>
      <p>Our absolute obsession with delivering quality software artifacts on time and in budget is what differentiates us from our competitors.We are able to live out this passion by partnering with our clients to ensure that the correct people, processes and technology are applied to each software development project.</p>
    </div>
  </main>

  <section class="features">
    <article class="feature">
      <div class="feature-head">
        <svg width="36" height="34" viewBox="0 0 36 34"><polygon points="18,1 22.5,12.5 35,12.8 25,20.5 28.6,33 18,25.8 7.4,33 11,20.5 1,12.8 13.5,12.5" fill="#d4d4d6" stroke="#bdbdbf"/></svg>
        <h2>Lorem ipsum dolor</h2>
      </div>
      <p>Lorem ipsum dolor sit amet, con-sectetuer adipiscing elit, sed diam nonummy nibh euismod tincidunt ut laoreet dolore magna aliquam erat volutpat. Ut wisi enim ad minim veniam, quis nostrud exerci tation ullamcorper suscipit lobortis nisl ut aliquip ex ea commodo consequat.</p>
      <span class="read-more">read more &gt;&gt;</span>
    </article>
    <article class="feature">
      <div class="feature-head">
        <svg width="36" height="36" viewBox="0 0 36 36"><rect x="2" y="6" width="24" height="28" fill="#f4f4f4" stroke="#bdbdbf"/><path d="M12 24 L30 4 L34 8 L16 28 L11 29 Z" fill="#d4d4d6" stroke="#a9a9ab"/></svg>
        <h2 style="margin-left:18px">Lorem ipsum dolor</h2>
      </div>
      <p>Lorem ipsum dolor sit amet, con-sectetuer adipiscing elit, sed diam nonummy nibh euismod tincidunt ut laoreet dolore magna aliquam erat volutpat. Ut wisi enim ad minim veniam</p>
      <span class="read-more">read more &gt;&gt;</span>
    </article>
    <article class="feature">
      <div class="feature-head">
        <svg width="36" height="34" viewBox="0 0 36 34"><polygon points="18,1 22.5,12.5 35,12.8 25,20.5 28.6,33 18,25.8 7.4,33 11,20.5 1,12.8 13.5,12.5" fill="#d4d4d6" stroke="#bdbdbf"/></svg>
        <h2>Lorem ipsum dolor</h2>
      </div>
      <p>Lorem ipsum dolor sit amet, con-sectetuer adipiscing elit, sed diam nonummy nibh euismod tincidunt ut laoreet dolore magna aliquam erat volutpat. Ut wisi enim ad minim veniam, quis nostrud exerci tation ullamcorper suscipit</p>
      <span class="read-more">read more &gt;&gt;</span>
    </article>
    <aside class="map-block">
      <h2>Find us on Mapway</h2>
      <div class="map-area" role="img" aria-label="Interactive street map showing the office location"></div>
    </aside>
  </section>

  <footer class="footer-nav">
    Home<span>|</span>Company<span>|</span>Professional services<span>|</span>Portfolio<span>|</span>Contact us
  </footer>
</body>
</html>
```